Two companies with one (great) goal... Need a Business card Design

Our Design consists of 2 companies with a common goal-- Embracing a Healthy Lifestyle!
1. The Vitality & Health Travel Trust- consists of a large ranch where horses, and crops of plants and vegetables are a significant component. Tourism developments are underway and the Ffoundation plays a significant role in supporting Sporting events.
2. Nuvacare is a manufacturer of medical and diagnostic equipment inclusive of small medical outposts throughout remote and rural regions of the country.

We are looking for a 2 sided business card with one company on each side. The ideal design will make the 2 different businesses flow together, while at the same time, also work if only one side was printed.

Information for Nuvacare Design:
Medical, Diagnostic and Laboratory Equipment | Medical Imaging Skyvault ScanHub | Biomedical Services
www.nuvacare.example
info@nuvacare.example
Tel: (389) 452) 1968

Information for The Vitality & Health Travel Trust:
DIRECTOR NAME
Corvale, Northern Coast
www.vitalitytrust.example
info@vitalitytrust.example
Tel: (507) 318-9275

*It is important that the font used is not too small please.

A few different color variations of each logo are included, any variation could be used.

Tagline is being finalized but ideally there would be a spot to add this in the future. Top tagline currently is "Healthy Lifestyle Through Better Living"

Industry/Entity Type

Medical

Requirements
Must have
• Font that is large enough to read

```html
<!DOCTYPE html>
<html lang="en">
<head>
<meta charset="utf-8">
<title>Vitality Trust &amp; Nuvacare Business Cards</title>
<link href="https://fonts.googleapis.com/css2?family=Arimo:wght@400;700&display=swap" rel="stylesheet">
<style>
  :root {
    --bg: #c9c9cb;
    --card: #ffffff;
    --ink: #1a1a1a;
    --gold-light: #f3d27a;
    --gold: #d8a437;
    --gold-dark: #a8741c;
    --black: #0d0d0d;
    --silver: #e6e6e6;
  }
  * { margin: 0; padding: 0; box-sizing: border-box; }
  html, body { width: 1200px; height: 960px; overflow: hidden; }
  body {
    background: var(--bg);
    font-family: "Arimo", Arial, sans-serif;
    color: var(--ink);
    position: relative;
  }
  .card {
    position: absolute;
    width: 560px;
    height: 330px;
    background: var(--card);
    border-radius: 22px;
    overflow: hidden;
    box-shadow: 0 10px 24px rgba(0,0,0,.25);
  }
  .card--trust { left: 90px; top: 80px; }
  .card--nuvacare { left: 550px; top: 540px; }

  .director { position: absolute; left: 24px; top: 24px; font-size: 15px; }

  .trust-mark { position: absolute; left: 100px; top: 24px; width: 400px; text-align: center; }
  .trust-mark__art {
    display: block; margin: 0 auto 8px; width: 170px; height: 78px; border-radius: 8px;
    background: linear-gradient(135deg, #2a2a2a, #777 60%, var(--gold) 100%);
  }
  .trust-mark__name { font-size: 24px; font-weight: 700; letter-spacing: 1px; line-height: 1.15; }

  .trust-web { position: absolute; left: 0; right: 0; top: 184px; text-align: center; font-size: 15px; }

  .contacts { position: absolute; list-style: none; font-size: 15px; }
  .contacts li { display: flex; align-items: center; gap: 8px; height: 24px; white-space: nowrap; }
  .contacts svg { width: 16px; height: 16px; fill: var(--ink); flex: none; }
  .card--trust .contacts { left: 312px; top: 210px; }
  .card--nuvacare .contacts { left: 340px; top: 196px; }

  .strip { position: absolute; left: 0; right: 0; bottom: 0; height: 14px; display: flex; }
  .strip__gold { width: 62%; background: linear-gradient(90deg, var(--gold-dark), var(--gold-light) 50%, var(--gold)); }
  .strip__silver { width: 55%; background: linear-gradient(90deg, var(--silver), #fff); }
  .strip__black { flex: 1; background: var(--black); }

  .nuva-mark { position: absolute; left: 120px; top: 62px; display: flex; align-items: center; gap: 14px; }
  .nuva-mark__name { font-size: 50px; font-weight: 700; letter-spacing: 2px; }
  .nuva-mark__square { width: 44px; height: 44px; background: var(--black); }
  .nuva-sub { position: absolute; left: 250px; top: 118px; font-size: 13px; }

  .nuva-lines { position: absolute; left: 0; right: 0; top: 148px; text-align: center; font-size: 14px; line-height: 1.45; }
</style>
</head>
<body>

<section class="card card--trust">
  <p class="director">DIRECTOR NAME</p>
  <div class="trust-mark">
    <span class="trust-mark__art" role="img" aria-label="Trust emblem artwork area: horse head illustration in black with a gold swoosh"></span>
    <p class="trust-mark__name">VITALITY &amp; HEALTH<br>TRAVEL TRUST</p>
  </div>
  <p class="trust-web">www.vitalitytrust.example</p>
  <ul class="contacts">
    <li><svg viewBox="0 0 16 16"><path d="M3 1h3l1.5 4-2 1.3a9 9 0 0 0 4.2 4.2L11 8.5 15 10v3a2 2 0 0 1-2 2A12 12 0 0 1 1 3a2 2 0 0 1 2-2z"/></svg>(507) 318-9275</li>
    <li><svg viewBox="0 0 16 16"><path d="M1 3h14v10H1zM2.5 4.5 8 9l5.5-4.5v-.2h-11z" fill-rule="evenodd"/></svg>info@vitalitytrust.example</li>
    <li><svg viewBox="0 0 16 16"><path d="M8 0a5.5 5.5 0 0 1 5.5 5.5C13.5 10 8 16 8 16S2.5 10 2.5 5.5A5.5 5.5 0 0 1 8 0zm0 3.3a2.2 2.2 0 1 0 0 4.4 2.2 2.2 0 0 0 0-4.4z" fill-rule="evenodd"/></svg>Corvale, Northern Coast</li>
  </ul>
  <div class="strip"><span class="strip__gold"></span><span class="strip__black"></span></div>
</section>

<section class="card card--nuvacare">
  <div class="nuva-mark">
    <span class="nuva-mark__name">NUVACARE</span>
    <span class="nuva-mark__square"></span>
  </div>
  <p class="nuva-sub">Biomedical Services</p>
  <p class="nuva-lines">Medical, Diagnostic and Laboratory Equipment<br>| Medical Imaging Skyvault ScanHub |</p>
  <ul class="contacts">
    <li><svg viewBox="0 0 16 16"><path d="M3 1h3l1.5 4-2 1.3a9 9 0 0 0 4.2 4.2L11 8.5 15 10v3a2 2 0 0 1-2 2A12 12 0 0 1 1 3a2 2 0 0 1 2-2z"/></svg>(389) 452) 1968</li>
    <li><svg viewBox="0 0 16 16"><path d="M8 1a7 7 0 1 0 0 14A7 7 0 0 0 8 1zm0 1.3c.8 0 1.8 1.6 2.1 4.2H5.9C6.2 3.9 7.2 2.3 8 2.3zM2.4 7.5h2.2c0 1 .1 1.9.3 2.7H3a5.7 5.7 0 0 1-.6-2.7zm9 0h2.2a5.7 5.7 0 0 1-.6 2.7h-1.9c.2-.8.3-1.7.3-2.7zm-5.5 0h4.2c0 1-.1 1.9-.3 2.7H6.2c-.2-.8-.3-1.7-.3-2.7zm.4 4h3.4C9.3 13 8.6 13.7 8 13.7s-1.3-.7-1.7-2.2z" fill-rule="evenodd"/></svg>www.nuvacare.example</li>
    <li><svg viewBox="0 0 16 16"><path d="M1 3h14v10H1zM2.5 4.5 8 9l5.5-4.5v-.2h-11z" fill-rule="evenodd"/></svg>info@nuvacare.example</li>
  </ul>
  <div class="strip"><span class="strip__silver"></span><span class="strip__black"></span></div>
</section>

</body>
</html>
```